Major Australian Food and Wine Event Web Design Project

The project will consist of 3 designs
The homepage
A city hub page
A general content page

The main audience who will visit the website will be (in Order of importance:

1) Visitors
- Mainly women 24 – 54 years (they are the main ticket buyers)
- In a relationship – so will go to the show with their partner
- In a good paying job or home maker – and who have disposable income to spend $30 a ticker
- Enjoy food, wine and going out
- Looking for a fun day out – although an event that is about food and wine – it is an event that most people will go to and have a fun day out – not too pretentious

A smaller proportion of the audience will be:
2) Exhibitors & sponsors ( both prospective and existing)
3) Media

Objectives:

- Functionality on home page and sub pages needs to be updated, clear, easy to navigate and inject a sense of ‘fun’ – need to make it look more professional
- Need to incorporate the many things that need to be on the home page and sub pages in a visually appealing manner
- Ensure the ‘Cons’ above are considered and reflected in functionality and design
- To not be too focus on the colours (these can be changed) – but focus on the functionality and overall design opportunities.

Approach:

Keywords to describe the Bright Plate & Vine Fair:
Fun day out, discover, learn, indulge, entertaining

Other website examples:

Some great consumers event websites from the UK really make our website look basic and juvenile – and below are some examples of the presentation of how we would like our website to look like:

http://www.morselfairs-example.com/london/ This website is clean, includes good social media integration and exudes a sense of fun. Their content pages, such as the features landing page also presents options in a clear and visually appealing way with a series of boxes including image and text http://www.morselfairs-example.com/london/content/343/Features

http://www.homecraftexpo-example.com/ - this is also a great website – and it incorporates all the elements we would be looking for on our homepage – but the background/skin also includes a sense of fun and cheekiness. Subpages also are consistent.

Features

• Its a fun day that offers great value for money
• Caters to all visitors, regardless of different levels of knowledge or interest in food, wine and cooking.
• Sample great quality food and wine products from hundreds of reputable exhibitors
• Learn more through many of the shows feature activities (Celeb Theatre, Wine Theatre, Cooking & Cheese Classes)

Functionality & Structure:

In a user friendly, easy to view way, we need to incorporate the following functionality elements on home page:
- main header (that will incorporate our current creative) with a ‘fun’ skin
- navigation tabs/references (hone, location, tickets, blog, sign up, exhibitors)
- navigation/content banner (rotating)
- Area for small intro about the show
- News and highlight section
- New exhibitors section
- Obvious Ticket call to action
- Obvious sign up call to action
- Social media buttons or links ( really like the moving gifs on the Homecraftexpo-example.com site
- area for advertising (MREC size) to sell to exhibitors/sponsors
- Show dates for all 5 shows (maybe in main header)

Subpage layout is also important and needs to reflect the homepage – so would also like to see examples of how this would look and tie in with navigation – we generally have a lot of content on these pages, so clear navigation would be useful. – see below for further details of functionality for city Hubs

‘CITY HUB’ BRIEF
When navigating to each location the user will be taken to a ‘CITY HUB’ which should replicate design and content elements of a main HOME page, as well as reflect more specific information for each Show. Elements which must appear on this page are:
• FEATURES – which may be displayed in categories (in boxes, see appendix 1.0) which will link through to relevant content pages. Or in one box which will link through to a features page with all presented in boxes
• CHEFS – may be displayed as a separate icon box which will link to chefs page with bios, Celeb Theatre timetable etc.
• TICKETS – either a button or clear callout to purchase tickets
• PLAN YOUR DAY – may be displayed in a separate content box which will then link through to getting there, sample itineraries and downloadable pocket show guide for visitors to print before coming to the Show.
• WHO’S EXHIBITING – to link back to city specific exhibitor lists

Our current website is out of date and has the following inadequacies (www.brightplatefair-example.com.au) -

The homepage
A city hub page
A general content page

1) Visitors

3) Media

Objectives:

Approach:

To be perceived as a fun, entertaining event with something for everyone - website creative and navigation must reflect this.

Other website examples:

Features

- New exhibitors section

‘CITY HUB’ BRIEF

- Dated design/layout
- Homepage too text heavy
- No content boxes that can be used for different features/areas (eg. News, Exhibitors etc)
- Uninspiring colours and skin(eg. grey background), does not reflect ‘a fun day out’
- Limited presence of social media platforms and lacks ‘community’
- No continuity in sub pages
- main banner too big – takes up too much space on homepage

Requirements
Must have
• As per above brief.

In addition:
Floating social media buttons on side
Wrap around image
Drop down menu (specifically for the location nav item)

```html
<!DOCTYPE html>
<html lang="en">
<head>
<meta charset="utf-8">
<title>Bright Plate &amp; Vine Fair – Melbourne</title>
<link href="https://fonts.googleapis.com/css2?family=Arimo:wght@400;700&family=Josefin+Sans:wght@300;400&family=Noto+Serif:wght@700&family=Oswald:wght@400;500&display=swap" rel="stylesheet">
<style>
:root{
  --red:#d8352a;
  --red-dark:#b32a20;
  --ink:#333;
  --muted:#666;
  --line:#dcdcdc;
  --panel:#f2f2f2;
  --footer:#e9e9e9;
  --dark:#3b3b3b;
  --link:#2a6aa8;
  --white:#fff;
}
*{box-sizing:border-box;margin:0;padding:0}
html,body{width:953px;height:1200px;overflow:hidden}
body{position:relative;font-family:Arimo,Arial,sans-serif;color:var(--ink);background:var(--footer);font-size:10px}
.abs{position:absolute}
.skin{left:0;top:0;width:953px;height:803px;background:linear-gradient(180deg,#6f9fcf 0%,#a9c8e4 22%,#d9e6ee 34%,#8aa663 48%,#4f7a2f 70%,#6d8a4c 88%,#b8b8a8 100%)}
.logo{left:136px;top:0;width:102px;height:72px;background:var(--white);box-shadow:0 1px 3px rgba(0,0,0,.3);display:flex;align-items:center;justify-content:center;text-align:center;font:700 13px/1.15 Arimo,Arial,sans-serif;color:var(--red);padding:6px}
.utility{left:578px;top:0;width:236px;height:19px;background:var(--dark);color:#ddd;font-size:10px;display:flex;align-items:center;justify-content:center;gap:5px;border-radius:0 0 3px 3px;white-space:nowrap}
.dates{font-size:10px;font-weight:700;color:#333;white-space:nowrap}
.dates span{font-weight:400}
.date-hi{background:#6a6a6a;color:#fff;padding:2px 5px}
.cta-signup{left:672px;top:38px;width:100px;height:31px;background:var(--red);color:#fff;font:500 13px/31px Oswald,sans-serif;text-align:center;border-radius:3px;box-shadow:0 2px 3px rgba(0,0,0,.3);white-space:nowrap}
.panel{left:122px;top:88px;width:708px;height:695px;background:var(--panel);box-shadow:0 0 6px rgba(0,0,0,.25);border-bottom:4px solid var(--red)}
.nav{left:129px;top:98px;width:697px;height:23px;font:300 16px/23px "Josefin Sans",sans-serif;color:#333;text-transform:uppercase}
.nav a{position:absolute;top:0;color:inherit;text-decoration:none;padding:0 7px;white-space:nowrap}
.nav .current{background:var(--red);color:#fff}
.nav .boxed{border:1px solid var(--red);color:var(--red);line-height:21px}
.hero-photo{left:128px;top:132px;width:434px;height:181px;background:linear-gradient(135deg,#7a6a58,#a99680 45%,#3c3a44)}
.hero-text{left:562px;top:132px;width:264px;height:181px;background:#4d4a47;color:#eee;padding:30px 22px}
.hero-text h1{font:300 22px "Josefin Sans",sans-serif;letter-spacing:.5px;margin-bottom:12px}
.hero-text p{font-size:9px;line-height:13px}
.tab-tickets{left:833px;top:166px;width:27px;height:109px;background:var(--red);border-radius:0 4px 4px 0;color:#fff;font:500 13px Oswald,sans-serif;writing-mode:vertical-rl;transform:rotate(180deg);text-align:center;line-height:27px}
.social-float{left:91px;top:166px;width:31px;height:113px;background:#fff;border-radius:4px 0 0 4px;box-shadow:-1px 1px 3px rgba(0,0,0,.25);padding:6px 5px;display:flex;flex-direction:column;gap:5px}
.social-float i{display:block;width:21px;height:21px;border-radius:3px}
.sidebar{left:136px;top:336px;width:200px}
.side-head{height:21px;background:#6e6e6e;color:#fff;font:400 12px/22px "Josefin Sans",sans-serif;padding-left:13px;text-transform:uppercase}
.side-list{list-style:none;background:#fff}
.side-list li{height:20px;border-bottom:1px solid #e3e3e3;font-size:9px;line-height:20px;padding-left:13px;color:#333}
.side-list .active{background:var(--red);color:#fff;width:212px;position:relative;font-weight:700}
.book{left:136px;top:562px;width:200px;height:64px;background:var(--red);color:#fff;text-align:center}
.book .inner{position:absolute;left:30px;top:10px;width:140px;height:44px;border:1px dashed rgba(255,255,255,.6)}
.book small{display:block;font:400 10px Oswald,sans-serif;margin-top:4px}
.book b{display:block;font:500 15px Oswald,sans-serif;letter-spacing:.5px}
.learn{left:136px;top:637px;width:200px;height:116px}
.learn-copy{position:absolute;left:0;top:0;width:84px;height:116px;background:var(--red);color:#fff;font:400 13px/19px Oswald,sans-serif;padding:9px 8px;text-transform:uppercase}
.learn-copy em{font-style:normal;font-size:8px;display:block;line-height:10px}
.learn-copy strong{font-weight:500;font-size:16px}
.learn-photo{position:absolute;left:84px;top:0;width:116px;height:116px;background:linear-gradient(160deg,#6f9a3c,#b84a2a 70%,#5a3a22)}
.crumb{left:355px;top:333px;font-size:9px;color:#555}
.crumb a{color:var(--red);text-decoration:none}
.tools{left:735px;top:333px;font-size:7px;color:#666;letter-spacing:.5px;white-space:nowrap}
.card{position:absolute;width:224px;height:122px;background:#fff;box-shadow:0 1px 2px rgba(0,0,0,.12);padding:13px 14px}
.card h2{font:700 13px "Noto Serif",Georgia,serif;color:#222;margin-bottom:8px;white-space:nowrap}
.card h2.hot{color:var(--red)}
.card p{width:98px;font-size:8.5px;line-height:12px;color:#444}
.card .more{display:block;margin-top:8px;font-size:8.5px;color:var(--link)}
.card .thumb{position:absolute;left:122px;top:38px;width:88px;height:68px;border:3px solid #fff;box-shadow:0 0 2px rgba(0,0,0,.4)}
.foot-title{font:400 12px "Josefin Sans",sans-serif;text-transform:uppercase;color:#333;white-space:nowrap}
.dash-box{position:absolute;border:2px dashed #c9c9c9;background:#f6f6f6}
.field{height:22px;background:#e5e5e5;border:1px solid #cfcfcf;margin-bottom:9px}
.btn-red{display:inline-block;background:var(--red);color:#fff;font:500 12px Oswald,sans-serif;padding:3px 14px;text-transform:uppercase}
.fb{left:622px;top:821px;width:208px;height:200px;background:#fff;border:1px solid #ccc;padding:8px}
.faces{display:grid;grid-template-columns:repeat(4,34px);gap:4px 8px;margin-top:6px}
.face .avatar{height:34px}
.face span{display:block;font-size:6.5px;color:#666;text-align:center;margin-top:2px;line-height:8px;white-space:nowrap}
.sponsors{left:130px;top:1066px;width:430px;height:64px;display:flex}
.sponsors div{flex:1;display:flex;align-items:center;justify-content:center;font:700 11px Arimo,Arial,sans-serif;color:#555;border-right:1px solid #d4d4d4;white-space:nowrap}
.sponsors div:last-child{border-right:0}
.legal{left:622px;top:1041px;width:200px;font-size:7px;line-height:10px;color:#666}
.bottom-line{left:0;top:1157px;width:953px;height:3px;background:#c8c8c8}
.foot-nav{left:122px;top:1171px;font:300 11px "Josefin Sans",sans-serif;color:#444;letter-spacing:.5px;white-space:nowrap}
.foot-social{top:1168px;width:20px;height:20px;border-radius:50%;background:#444}
</style>
</head>
<body>

<div class="abs skin" role="img" aria-label="Sky and rolling vineyard scenery wrapping the page"></div>

<header>
  <div class="abs logo">Bright Plate &amp; Vine Fair</div>
  <nav class="abs utility">Contact Us | Exhibitor Info | About Us | Sponsors</nav>
  <div class="abs dates" style="left:327px;top:41px">Melbourne <span>- June 1-3</span></div>
  <div class="abs dates" style="left:438px;top:39px"><span class="date-hi">Adelaide - October 12-14</span></div>
  <div class="abs dates" style="left:580px;top:41px">Perth <span>- July 13-15</span></div>
  <div class="abs dates" style="left:327px;top:59px">Sydney <span>- June 22-24</span></div>
  <div class="abs dates" style="left:443px;top:59px">Brisbane <span>- November 9-11</span></div>
  <div class="abs cta-signup">SIGN UP IT'S FREE</div>
</header>

<div class="abs social-float">
  <i style="background:#3fa9dd"></i><i style="background:#3b5b98"></i><i style="background:#c4302b"></i><i style="background:#e9e9e9;border:1px solid #ccc"></i>
</div>
<div class="abs tab-tickets">GET TICKETS</div>

<main class="abs panel"></main>

<nav class="abs nav">
  <a class="current" style="left:0">Home</a>
  <a style="left:94px">Location</a>
  <a class="boxed" style="left:218px">Tickets</a>
  <a style="left:341px">Blog</a>
  <a style="left:429px">Sign Up</a>
  <a style="left:532px">Want to Exhibit?</a>
</nav>

<section>
  <div class="abs hero-photo" role="img" aria-label="Two smiling chefs standing in a restaurant kitchen"></div>
  <div class="abs hero-text">
    <h1>MELBOURNE</h1>
    <p>Elmstead Park hosted 50,000 people across 4 days from 16-19 June 2011, which featured world-class chefs, 40 of Harbourton's top restaurants and over 200 hand-picked foodie exhibitors to shop from. Check out our visiting guide to discover all about Savour.</p>
  </div>
</section>

<aside class="abs sidebar">
  <div class="side-head">Melbourne</div>
  <ul class="side-list">
    <li>Beef Recipes</li><li>Chicken Recipes</li><li>Chocolate Recipes</li><li>Fish Recipes</li>
    <li class="active">Chocolate Recipes</li>
    <li>Beef Recipes</li><li>Chicken Recipes</li><li>Chocolate Recipes</li><li>Fish Recipes</li>
  </ul>
</aside>

<div class="abs book"><div class="inner"><small>CLICK HERE TO</small><b>BOOK A TICKET</b></div></div>

<div class="abs learn">
  <div class="learn-copy">Learn<br>Cooking<br>Recipes<em>by our</em><strong>Experts</strong></div>
  <div class="learn-photo" role="img" aria-label="Fresh salad leaves and grilled steak"></div>
</div>

<div class="abs crumb"><a>Home</a> → Visitings</div>
<div class="abs tools">✉ SEND &nbsp;&nbsp; ⤴ SHARE</div>

<article class="card" style="left:354px;top:357px"><h2>Celebrity Chef Theater</h2><p>Centrally located in Elmstead Park, it's easy to get to Savour.</p><a class="more">Read More →</a><div class="thumb" style="background:linear-gradient(135deg,#ddd,#8a7c70)" role="img" aria-label="Two chefs on stage"></div></article>
<article class="card" style="left:593px;top:357px"><h2>Features &amp; Masterclasses</h2><p>Centrally located in Elmstead Park, it's easy to get to Savour.</p><a class="more">Read More →</a><div class="thumb" style="background:linear-gradient(135deg,#c98a5a,#e8e0c8)" role="img" aria-label="Plated dishes on a table"></div></article>
<article class="card" style="left:354px;top:493px"><h2 class="hot">Plan Your Day</h2><p>Centrally located in Elmstead Park, it's easy to get to Savour.</p><a class="more">Read More →</a><div class="thumb" style="background:linear-gradient(135deg,#3f5a4a,#c9a77a)" role="img" aria-label="Visitors tasting food at a stall"></div></article>
<article class="card" style="left:593px;top:493px"><h2>Exhibitors</h2><p>Centrally located in Elmstead Park, it's easy to get to Savour.</p><a class="more">Read More →</a><div class="thumb" style="background:linear-gradient(135deg,#f3f3f3,#d8352a)" role="img" aria-label="Exhibitor stand signage"></div></article>
<article class="card" style="left:354px;top:629px"><h2>Visiting the Show</h2><p>Centrally located in Elmstead Park, it's easy to get to Savour.</p><a class="more">Read More →</a><div class="thumb" style="background:linear-gradient(135deg,#2c3a6a,#c8b090)" role="img" aria-label="Crowd at the show entrance"></div></article>
<article class="card" style="left:593px;top:629px"><h2>Tickets</h2><p>Centrally located in Elmstead Park, it's easy to get to Savour.</p><a class="more">Read More →</a><div class="thumb" style="background:linear-gradient(135deg,#8a3a8a,#4a6ad0)" role="img" aria-label="Fanned show tickets"></div></article>

<footer>
  <div class="abs foot-title" style="left:122px;top:819px">Subcribe Us</div>
  <div class="dash-box" style="left:122px;top:840px;width:239px;height:181px;padding:22px 16px">
    <p style="font-size:9px;line-height:13px;color:#555;margin-bottom:14px">Join the club and get exclusive recipes, discounts and more!</p>
    <div class="field"></div><div class="field"></div>
    <span class="btn-red" style="margin-top:8px">Submit</span>
  </div>

  <div class="abs foot-title" style="left:372px;top:819px">Latest Quick Tip</div>
  <div class="dash-box" style="left:372px;top:840px;width:238px;height:181px;padding:10px 14px">
    <div style="font:500 30px Oswald,sans-serif;color:#333">#14</div>
    <div style="height:1px;background:#ccc;margin:4px 0 10px"></div>
    <p style="font-size:9px;line-height:13px;color:#555;margin-bottom:12px">Our food is inspired by cuisines across the Mediterranean. From the finest pastries to fresh seafood there's something to suit every taste and occasion.Our food is inspired by cuisines across.</p>
    <span class="btn-red">More Tips</span>
  </div>

  <div class="abs fb">
    <div style="font-size:8px;color:#3b5998;font-weight:700">Bright Plate &amp; Vine Fair <span style="font-weight:400;color:#666">on Friendbook</span></div>
    <div style="display:inline-block;margin-top:4px;font-size:7px;border:1px solid #ccc;padding:1px 5px;background:#eee">Like</div>
    <div style="border-top:1px solid #ddd;margin-top:8px;padding-top:5px;font-size:7px;color:#555">36,943 people like <b>Olivara</b>.</div>
    <div class="faces">
      <div class="face"><div class="avatar" style="background:#b89a80" role="img" aria-label="Member avatar"></div><span>Rani</span></div>
      <div class="face"><div class="avatar" style="background:#c8b8a8" role="img" aria-label="Member avatar"></div><span>Mira</span></div>
      <div class="face"><div class="avatar" style="background:#9aa8b8" role="img" aria-label="Member avatar"></div><span>Tomas</span></div>
      <div class="face"><div class="avatar" style="background:#6a8ab0" role="img" aria-label="Member avatar"></div><span>Olly</span></div>
      <div class="face"><div class="avatar" style="background:#a88a70" role="img" aria-label="Member avatar"></div><span>Hugo</span></div>
      <div class="face"><div class="avatar" style="background:#c09080" role="img" aria-label="Member avatar"></div><span>Nela</span></div>
      <div class="face"><div class="avatar" style="background:#8a7a6a" role="img" aria-label="Member avatar"></div><span>Pero</span></div>
      <div class="face"><div class="avatar" style="background:#b0a090" role="img" aria-label="Member avatar"></div><span>Jolie</span></div>
    </div>
    <div style="position:absolute;left:8px;bottom:8px;font-size:6.5px;color:#555">■ Friendbook social plugin</div>
  </div>

  <div class="abs foot-title" style="left:322px;top:1043px">Our Sponsors</div>
  <div class="abs sponsors">
    <div>Crustline</div><div>Bun Monarch</div><div>Pie Hutch</div><div>Sandwell</div><div>Coop &amp; Co</div>
  </div>

  <div class="abs legal">
    <div style="font:700 9px Arimo,Arial,sans-serif;color:var(--red);margin-bottom:4px">Bright Plate &amp; Vine Fair</div>
    © 2011 brightplatefair-example.com<br>Organized by Ten Tables Media Ltd.<br>Home Craft Live is a trademark of Tidewell Media Limited.<br>Licenced by Tidewell Media Enterprises.
  </div>

  <div class="abs bottom-line"></div>
  <nav class="abs foot-nav">HOME | LOCATION | TICKETS | BLOG | SIGN UP | WANT TO EXHIBIT?</nav>
  <div class="abs foot-social" style="left:781px"></div>
  <div class="abs foot-social" style="left:805px"></div>
</footer>

</body>
</html>
```